WordPress website in children books redesign

We are personalised children storybook creators with a range of personalized books, music CDs and DVDs that are created for each child. We sell our concept through a license via distributors / entrepreneurs mainly based in France and Europe. We want to focus on selling B2C to parents and grandparents, looking to buy presents to their children aged 0 to 10 years old. Those present are educative, unique for each child, and they will learn to have fun and learn to have fun. I would like to redesign our WordPress website https://brightpebbletales.co.uk/index.php We are a children in the world of books and music books: books, music CDs and DVDs looking for something a little more along the lines of our competitors. See ike www.glimmerpage.com, www.tovikoro.com, www.lefiletdesetoiles.com, https://www.lespetitsvergers.com/, https://plumquestkids.com/ Our current website is a bit too old fashioned so I am looking at a much more modern design Here is a link for a few products that are not available here: https://www.filecrate.example/sh/kq417ptobnrelwx/ZZQ4rTfLmN8y-aBcDeFgHiJ-kl?dl=0 We have 2 sides in our website: B2C on the left side and B2B on the right site; B2B is for distributors that are entrepreneurs buying our concept. for the homepage design, the main focus will be B2Consumer Our current page is too blended, lacks reassurance elements and I would like to have a look at this page. from our current stories. here is a link for our business book to give you a feel for it: http://online.pagewhirl.example/qtpd/mnvs/ MAIN PAGES TO REVIEW / HOMEPAGE / https://brightpebbletales.co.uk/ BOOKS: https : //brightpebbletales.co.uk/product-category/personalised-books/ MUSIC: https://brightpebbletales.co.uk/product-category/music-cds/ BLOG: https://brightpebbletales.co.uk/blog -2 / Looking forward to seeing you and your questions asap

Target Market(s)

parents and grandparents of children aged 0 to 10 years old. This is for the European market

Industry/Entity Type

Publishing Company

Number of Pages Required

4 page

Colors
0392cd
9bcb3b
ec1f27
757575

Requirements
Must have
• keep within the color code of our RGB logo: D25028 RGB: 8CC364 329BC8 808285
Nice to have
• be more with the style of our competitors. Bright Pebble Tales am about making children learn the fun way, and develop their morality, self-esteem and confidence. It's about the magic of reading to help children learn while having fun. I have attached visuals but those are just examples and you we encourage you to suggest other ideas

```html
<!DOCTYPE html>
<html lang="en">
<head>
<meta charset="utf-8">
<title>Bright Pebble Tales – Personalised Books, Music &amp; DVDs</title>
<link rel="stylesheet" href="https://fonts.googleapis.com/css2?family=Fredoka:wght@500;600;700&family=Montserrat:wght@400;500;600;700&display=swap">
<style>
:root{
  --blue:#0392cd;
  --blue-dark:#1d5fa8;
  --green:#8cc364;
  --green-deep:#5fae36;
  --lime:#9bcb3b;
  --red:#ec1f27;
  --orange:#f7941d;
  --pink:#e5288f;
  --teal:#2bb48f;
  --grey:#757575;
  --ink:#333;
  --cream:#f2efcd;
  --white:#fff;
  --footer:#3f7d2a;
}
*{box-sizing:border-box;margin:0;padding:0}
html,body{width:1200px;height:4265px;overflow:hidden}
body{position:relative;background:var(--cream);font-family:"Montserrat",sans-serif;color:var(--ink)}
.abs{position:absolute}
.heading{font-family:"Fredoka",sans-serif;font-weight:600}
.placeholder{position:absolute}

/* header */
.site-header{position:absolute;left:0;top:0;width:1200px;height:150px;background:var(--white);z-index:3}
.brand{position:absolute;left:136px;top:14px;width:172px;height:172px;border-radius:50%;background:var(--white);box-shadow:0 2px 8px rgba(0,0,0,.15);display:flex;align-items:center;justify-content:center;text-align:center;z-index:5}
.brand span{font-family:"Fredoka",sans-serif;font-weight:600;font-size:26px;line-height:1.1;color:var(--blue-dark)}
.main-nav{position:absolute;left:336px;top:100px;display:flex;gap:6px;z-index:4}
.main-nav a{display:block;height:50px;line-height:50px;padding:0 16px;font-family:"Fredoka",sans-serif;font-weight:500;font-size:17px;color:var(--white);text-decoration:none;text-transform:uppercase;border-radius:6px 6px 0 0;transform:rotate(-2deg);white-space:nowrap}
.main-nav a:first-child{text-transform:none}
.cart{position:absolute;left:686px;top:34px}
.cart-count{position:absolute;left:706px;top:32px;width:14px;height:14px;border-radius:50%;background:var(--red);color:#fff;font-size:9px;text-align:center;line-height:14px}
.btn-register{position:absolute;left:745px;top:28px;width:172px;height:40px;border-radius:20px;background:var(--orange);color:#fff;font-family:"Fredoka",sans-serif;font-weight:600;font-size:15px;text-align:center;line-height:40px;border:2px solid #fbd199;white-space:nowrap}
.social{position:absolute;top:31px;width:34px;height:34px;border-radius:50%}

/* hero */
.hero{position:absolute;left:0;top:150px;width:1200px;height:547px;background:linear-gradient(100deg,#c9b69a 0%,#a78e6e 45%,#6f9bc4 75%,#2f68b4 100%)}
.hero-band{position:absolute;left:0;height:56px;display:flex;align-items:center;padding-left:142px;font-family:"Fredoka",sans-serif;font-weight:600;font-size:31px;color:#fff;text-transform:uppercase;letter-spacing:.3px;white-space:nowrap;clip-path:polygon(0 0,100% 0,96% 50%,100% 100%,0 100%)}
.hero-arrow{position:absolute;top:240px;width:34px;height:34px;border-radius:50%;background:#222;display:flex;align-items:center;justify-content:center}

/* welcome */
.welcome-title{position:absolute;left:0;top:755px;width:1200px;text-align:center;font-size:50px;color:#3a3a3a}
.welcome-text{position:absolute;left:160px;top:836px;width:880px;text-align:center;font-size:14px;line-height:27px;color:var(--grey)}
.feature{position:absolute;top:1024px;width:286px;height:365px;border-radius:18px;transform:rotate(-1.5deg);text-align:center;color:#fff;box-shadow:0 6px 0 rgba(0,0,0,.12)}
.feature-photo{position:absolute;left:57px;top:-30px;width:172px;height:172px;border-radius:50%;border:6px solid #fff}
.feature h3{position:absolute;left:0;width:100%;top:168px;font-size:28px;white-space:nowrap}
.feature p{position:absolute;left:28px;width:230px;top:212px;font-size:13px;line-height:20px}
.pill{display:inline-block;background:#fff;color:var(--ink);border-radius:16px;font-size:13px;font-weight:600;padding:7px 22px}
.feature .pill{position:absolute;left:93px;top:302px}

/* personalisation band */
.band{position:absolute;left:0;top:1470px;width:1200px;height:660px}
.video{position:absolute;left:165px;top:1641px;width:398px;height:322px;border-radius:30px;border:4px solid #fff;background:linear-gradient(135deg,#3a3a3a,#5b4a70 60%,#2c2c2c)}
.play{position:absolute;left:166px;top:128px;width:60px;height:60px;border-radius:50%;background:rgba(255,255,255,.85);display:flex;align-items:center;justify-content:center}
.band-title{position:absolute;left:606px;top:1648px;width:480px;font-size:32px;line-height:41px;color:#fff;text-transform:uppercase}
.band-text{position:absolute;left:606px;top:1782px;width:440px;font-size:15px;line-height:27px;color:#f3f8e8}
.btn-outline{position:absolute;left:606px;top:1910px;width:126px;height:36px;border:2px solid #fff;color:#fff;font-size:14px;font-weight:600;text-align:center;line-height:32px}

/* values */
.value{position:absolute;top:2185px;width:300px;text-align:center}
.value-icon{width:116px;height:116px;margin:0 auto;border-radius:14px}
.value h3{margin-top:38px;font-family:"Montserrat",sans-serif;font-weight:700;font-size:20px;color:#333}
.value p{margin:14px auto 0;width:290px;font-size:13px;line-height:24px;color:var(--grey)}
.btn-small{display:inline-block;margin-top:22px;border:2px solid #555;border-radius:16px;padding:5px 22px;font-size:12px;font-weight:600;color:#333}

/* products */
.products{position:absolute;left:0;top:2620px;width:1200px;height:640px;background:#fbfaf5}
.section-title{position:absolute;left:0;width:1200px;text-align:center;font-size:46px;color:#222;text-transform:uppercase}
.product{position:absolute;top:2807px;width:208px;height:364px;background:#fff;border:2px solid #e6e6e6;border-radius:26px;text-align:center}
.product-cover{width:120px;height:192px;margin:26px auto 0;border-radius:4px}
.product p{margin:20px auto 0;width:170px;font-size:14px;line-height:21px;color:#333}
.stars{margin-top:12px;color:var(--red);font-size:15px;letter-spacing:2px}
.price{margin-top:6px;font-weight:700;font-style:italic;color:var(--red);font-size:16px}

/* events */
.event-photo{position:absolute;top:3450px;width:184px;height:184px;border-radius:50%;border:6px solid var(--blue)}
.event-text{position:absolute;top:3458px;width:246px;font-size:14px;line-height:24px;color:#444}
.event-date{position:absolute;top:3595px;font-size:15px;font-weight:700;font-style:italic;color:#333;white-space:nowrap}
.mini-arrow{position:absolute;top:3400px;width:22px;height:22px;border-radius:50%;border:1.5px solid #999;display:flex;align-items:center;justify-content:center}

/* quote & contact */
.contact-zone{position:absolute;left:0;top:3711px;width:1200px;height:384px;background:#fff}
.block-title{position:absolute;top:3790px;font-size:28px;color:#222;text-transform:uppercase}
.field{position:absolute;width:212px;height:38px;border:1px solid #cfcfcf;border-radius:2px;font-size:12px;color:#666;padding:11px 12px;background:#fff}
.btn-submit{position:absolute;left:179px;top:3962px;width:212px;height:32px;background:var(--blue);color:#fff;font-weight:700;font-size:14px;text-align:center;line-height:32px}
.contact-line{position:absolute;left:690px;font-size:14px;line-height:20px;color:#333}
.fence{position:absolute;left:0;top:3985px;width:1200px;height:110px;background:linear-gradient(#ffffff 0%,#eef1ea 55%,#cfd9c4 100%)}

/* footer */
.site-footer{position:absolute;left:0;top:4095px;width:1200px;height:170px;background:var(--footer);color:#fff;text-align:center}
.site-footer .copy{position:absolute;left:0;top:48px;width:100%;font-size:13px;font-weight:500}
.site-footer .links{position:absolute;left:0;top:80px;width:100%;font-size:12px}
.foot-social{position:absolute;top:120px;width:30px;height:30px;border-radius:50%;border:1.5px solid #fff}
</style>
</head>
<body>

<!-- header -->
<header class="site-header">
  <svg class="cart" width="24" height="24" viewBox="0 0 24 24" fill="none" stroke="#ec1f27" stroke-width="2"><path d="M3 4h3l2 11h11l2-8H7"/><circle cx="10" cy="19" r="1.6"/><circle cx="17" cy="19" r="1.6"/></svg>
  <span class="cart-count">0</span>
  <div class="btn-register">ONLINE REGISTRATION</div>
  <span class="social" style="left:938px;background:#3b5a9a" aria-label="Social link"></span>
  <span class="social" style="left:981px;background:#2aa3ef" aria-label="Social link"></span>
  <span class="social" style="left:1030px;background:#d6201f" aria-label="Social link"></span>
  <nav class="main-nav">
    <a style="background:var(--blue-dark)">Home</a>
    <a style="background:var(--lime)">About us</a>
    <a style="background:var(--red)">Our products</a>
    <a style="background:var(--orange)">Distributors</a>
    <a style="background:var(--teal)">Gallery</a>
    <a style="background:var(--pink)">Blog</a>
    <a style="background:var(--blue)">Contact us</a>
  </nav>
</header>
<div class="brand"><span>Bright<br>Pebble<br>Tales</span></div>

<!-- hero -->
<section class="hero" role="img" aria-label="Photo of a child in an aviator cap and cape playing pilot in a cardboard box">
  <div class="hero-band" style="top:163px;width:500px;background:var(--blue)">When children</div>
  <div class="hero-band" style="top:228px;width:560px;background:var(--green-deep)">Become the heroes</div>
  <div class="hero-band" style="top:293px;width:610px;background:var(--red)">Of their own stories</div>
  <div class="hero-arrow" style="left:40px"><svg width="14" height="14" viewBox="0 0 14 14"><path d="M9 2 4 7l5 5" stroke="#fff" stroke-width="2" fill="none"/></svg></div>
  <div class="hero-arrow" style="left:1124px"><svg width="14" height="14" viewBox="0 0 14 14"><path d="M5 2l5 5-5 5" stroke="#fff" stroke-width="2" fill="none"/></svg></div>
</section>

<!-- welcome -->
<h1 class="welcome-title heading">Welcome to Bright Pebble Tales</h1>
<p class="welcome-text">Lorem ipsum dolor sit amet, consectetur adipiscing elit, sed do eiusmod tempor incididunt ut labore et dolore magna aliqua. Ut enim ad minim veniam, quis nostrud exercitation ullamco laboris nisi ut aliquip ex ea commodo consequat. Duis aute irure dolor in reprehenderit in voluptate velit esse cillum dolore eu fugiat nulla pariatur. Excepteur sint occaecat cupidatat non proident, sunt in culpa qui officia deserunt mollit anim id est laborum</p>

<article class="feature" style="left:148px;background:var(--orange)">
  <div class="feature-photo" role="img" aria-label="Photo of a smiling boy holding a book" style="background:linear-gradient(#d9a272,#8a5a3a)"></div>
  <h3 class="heading">Personalised books</h3>
  <p>Nemo enim ipsam voluptatem quia voluptas sit aspernatur aut odit aut fugit, sed quia consequ mag</p>
  <span class="pill">Read More</span>
</article>
<article class="feature" style="left:456px;background:#42a6d9">
  <div class="feature-photo" role="img" aria-label="Photo of a girl singing with headphones" style="background:linear-gradient(#f3c9d7,#e38aa8)"></div>
  <h3 class="heading">Music</h3>
  <p>Nemo enim ipsam voluptatem quia voluptas sit aspernatur aut odit aut fugit, sed quia consequ mag</p>
  <span class="pill">Read More</span>
</article>
<article class="feature" style="left:766px;background:var(--green-deep)">
  <div class="feature-photo" role="img" aria-label="Photo of a child playing with a toy truck" style="background:linear-gradient(#c9d6e0,#b5473a)"></div>
  <h3 class="heading">DVD cartoon</h3>
  <p>Nemo enim ipsam voluptatem quia voluptas sit aspernatur aut odit aut fugit, sed quia consequ mag</p>
  <span class="pill">Read More</span>
</article>
<div class="placeholder" role="img" aria-label="Illustration of two children holding hands" style="left:1052px;top:1392px;width:118px;height:118px;background:linear-gradient(#e8b15a,#3f6fb5);border-radius:10px;opacity:.8"></div>

<!-- personalisation band -->
<svg class="band" viewBox="0 0 1200 660" preserveAspectRatio="none" aria-hidden="true">
  <path d="M0 40 C200 0 380 70 600 40 S1000 0 1200 40 V620 C1000 660 820 600 600 630 S200 660 0 620 Z" fill="#79bb47"/>
</svg>
<div class="video" role="img" aria-label="Video still of hands opening a personalised storybook">
  <div class="play"><svg width="22" height="24" viewBox="0 0 22 24"><path d="M4 2l16 10L4 22z" fill="#333"/></svg></div>
</div>
<h2 class="band-title heading">Personalisation improves a child's learning ability and motivation</h2>
<p class="band-text">Bright Pebble Tales personalised books offers the possibility of sharing magical and unique moments which help the child become familiar with reading and inspire reading passion. Which is more special and magical</p>
<div class="btn-outline">READ MORE</div>

<!-- vision / mission / distributors -->
<div class="value" style="left:129px">
  <div class="value-icon" role="img" aria-label="Illustration of an abacus" style="background:linear-gradient(#3d4a5c,#e0a53a)"></div>
  <h3>OUR VISION</h3>
  <p>is to make children the heroes of the adventure &amp; live magical &amp; unforgettable moments they can share with their family and friends. Scenarios are</p>
  <span class="btn-small">READ MORE</span>
</div>
<div class="value" style="left:450px">
  <div class="value-icon" role="img" aria-label="Illustration of coloured crayons" style="background:linear-gradient(90deg,#e86a8f,#4aa3d8,#f0b43a)"></div>
  <h3>OUR MISSION</h3>
  <p>Personalisation offers for children to have an opportunity to recognise themselves in the story, thus developing the morale, self-esteem and confidence.</p>
  <span class="btn-small">READ MORE</span>
</div>
<div class="value" style="left:772px">
  <div class="value-icon" role="img" aria-label="Illustration of a toy train" style="background:linear-gradient(#e84a3a,#f4c23a 60%,#3a8fd0)"></div>
  <h3>DISTRIBUTORS</h3>
  <p>is to make children the heroes of the adventure &amp; live magical &amp; unforgettable moments they can share with their family and friends. Scenarios are</p>
  <span class="btn-small">READ MORE</span>
</div>

<!-- products -->
<section class="products">
  <svg class="abs" style="left:0;top:-20px" width="1200" height="60" viewBox="0 0 1200 60" preserveAspectRatio="none" aria-hidden="true"><path d="M0 40 C200 0 400 60 600 30 S1000 0 1200 30 V60 H0Z" fill="#fbfaf5"/></svg>
</section>
<div class="placeholder" role="img" aria-label="Illustration of a playground swing" style="left:56px;top:2550px;width:120px;height:125px;background:linear-gradient(#3aa0d8,#e8553a);border-radius:6px;opacity:.85"></div>
<h2 class="section-title heading" style="top:2700px">Our Products</h2>

<div class="product" style="left:148px">
  <div class="product-cover" role="img" aria-label="Book cover with a dinosaur" style="background:linear-gradient(#8cbf4a,#3f7d2a)"></div>
  <p>Sed ut perspiciatis unde omnis iste natus</p>
  <div class="stars">★★★★★</div><div class="price">$305.99</div>
</div>
<div class="product" style="left:378px">
  <div class="product-cover" role="img" aria-label="Book cover with a dragon" style="background:linear-gradient(#7a6fc4,#3a4e9e)"></div>
  <p>Sed ut perspiciatis unde omnis iste natus</p>
  <div class="stars">★★★★★</div><div class="price">$305.99</div>
</div>
<div class="product" style="left:612px">
  <div class="product-cover" role="img" aria-label="Book cover with farm animals" style="background:linear-gradient(#f0b640,#6fae3a)"></div>
  <p>Sed ut perspiciatis unde omnis iste natus</p>
  <div class="stars">★★★★★</div><div class="price">$305.99</div>
</div>
<div class="product" style="left:845px">
  <div class="product-cover" role="img" aria-label="Book cover with a Christmas scene" style="background:linear-gradient(#2f4fa8,#d2302a)"></div>
  <p>Sed ut perspiciatis unde omnis iste natus</p>
  <div class="stars">★★★★★</div><div class="price">$305.99</div>
</div>
<div class="placeholder" role="img" aria-label="Illustration of a seesaw" style="left:960px;top:3185px;width:180px;height:140px;background:linear-gradient(#3a8fd0,#f29a2e);border-radius:8px;opacity:.85"></div>

<!-- events -->
<svg class="abs" style="left:0;top:3230px" width="1200" height="40" viewBox="0 0 1200 40" preserveAspectRatio="none" aria-hidden="true"><path d="M0 10 C250 40 450 0 700 20 S1050 40 1200 15 V40 H0Z" fill="var(--cream)"/></svg>
<h2 class="section-title heading" style="top:3338px;font-size:40px">Latest Events</h2>
<div class="mini-arrow" style="left:572px"><svg width="8" height="8" viewBox="0 0 8 8"><path d="M5.5 1 2.5 4l3 3" stroke="#777" fill="none"/></svg></div>
<div class="mini-arrow" style="left:598px"><svg width="8" height="8" viewBox="0 0 8 8"><path d="M2.5 1l3 3-3 3" stroke="#777" fill="none"/></svg></div>

<div class="event-photo" role="img" aria-label="Photo of a boy reading a book" style="left:148px;background:linear-gradient(#e9c07a,#6b4a2e)"></div>
<p class="event-text" style="left:358px">Lorem ipsum dolor sit amet, consectetur adipiscing elit, sed do eiusmod tempor incididunt ut labore et dolore magna aliqua Ut enim ad minim veniam</p>
<div class="event-date" style="left:358px">Jan 21, 2017 \ 2 comments</div>
<div class="event-photo" role="img" aria-label="Photo of a grandparent reading with a child" style="left:623px;background:linear-gradient(#b9c9d8,#5f7a96)"></div>
<p class="event-text" style="left:833px">Lorem ipsum dolor sit amet, consectetur adipiscing elit, sed do eiusmod tempor incididunt ut labore et dolore magna aliqua Ut enim ad minim veniam unde omnis, consequuntur.</p>
<div class="event-date" style="left:833px">Jan 21, 2017 \ 2 comments</div>

<!-- quote & contact -->
<section class="contact-zone">
  <svg class="abs" style="left:0;top:-18px" width="1200" height="40" viewBox="0 0 1200 40" preserveAspectRatio="none" aria-hidden="true"><path d="M0 20 C300 0 500 35 800 15 S1100 0 1200 20 V40 H0Z" fill="#fff"/></svg>
</section>
<div class="fence" role="img" aria-label="Illustration of a white picket fence on grass"></div>
<div class="placeholder" role="img" aria-label="Illustration of a little girl in a colourful dress" style="left:14px;top:3765px;width:140px;height:330px;background:linear-gradient(#f3c0cf,#e05a8a 60%,#4aa0d6);border-radius:60px 60px 10px 10px;opacity:.85"></div>

<h2 class="block-title heading" style="left:179px">Get a Quote</h2>
<div class="field" style="left:179px;top:3856px">Your Name</div>
<div class="field" style="left:405px;top:3856px">Your E-Mail</div>
<div class="field" style="left:179px;top:3907px">Your Phone</div>
<div class="field" style="left:405px;top:3907px">Message</div>
<div class="btn-submit">SUBMIT</div>

<h2 class="block-title heading" style="left:657px">Contact Us</h2>
<svg class="abs" style="left:662px;top:3858px" width="14" height="18" viewBox="0 0 14 18"><path d="M7 1a6 6 0 0 0-6 6c0 4.5 6 10 6 10s6-5.5 6-10a6 6 0 0 0-6-6z" fill="var(--blue)"/><circle cx="7" cy="7" r="2.2" fill="#fff"/></svg>
<p class="contact-line" style="top:3856px">Bright Pebble Tales<br>Larkford, Hollin Vale District,<br>Ontario K7Q 2M8</p>
<svg class="abs" style="left:662px;top:3924px" width="15" height="15" viewBox="0 0 24 24"><path d="M6.6 10.8a15 15 0 0 0 6.6 6.6l2.2-2.2c.3-.3.7-.4 1-.2 1.1.4 2.3.6 3.6.6.6 0 1 .4 1 1V20c0 .6-.4 1-1 1A17 17 0 0 1 3 4c0-.6.4-1 1-1h3.5c.6 0 1 .4 1 1 0 1.2.2 2.4.6 3.6.1.3 0 .7-.2 1z" fill="var(--blue)"/></svg>
<p class="contact-line" style="top:3922px">Phone: 416-555-0142<br>905-555-0178</p>
<svg class="abs" style="left:662px;top:3970px" width="15" height="12" viewBox="0 0 15 12"><rect x=".5" y=".5" width="14" height="11" fill="var(--blue)"/><path d="M1 1l6.5 5L14 1" stroke="#fff" fill="none"/></svg>
<p class="contact-line" style="top:3966px">info@brightpebbletales.co.uk</p>

<div class="abs" style="left:912px;top:3800px;width:140px;height:140px;border-radius:50%;background:#fff;border:2px dashed #ccc;display:flex;align-items:center;justify-content:center;text-align:center">
  <span style="font-family:'Fredoka',sans-serif;font-weight:600;font-size:22px;line-height:1.1;color:var(--blue-dark)">Bright<br>Pebble<br>Tales</span>
</div>

<!-- footer -->
<footer class="site-footer">
  <p class="copy">© COPYRIGHT 2019 BRIGHT PEBBLE TALES. ALL RIGHTS RESERVED.</p>
  <p class="links">OUR PRODUCTS | ABOUT US | DISTRIBUTORS | BLOG | CONTACT</p>
  <span class="foot-social" style="left:533px"></span>
  <span class="foot-social" style="left:568px"></span>
  <span class="foot-social" style="left:603px"></span>
  <span class="foot-social" style="left:638px"></span>
</footer>

</body>
</html>
```